Clara Whitfield: Adult Models Flyer

We need an attractive flyer design to promote our adult modeling agency and recruit models to our business. We hire beautiful, young women and couples to be on a live adult camshow. We would like to highlight the following features of this job position:

-Pays $100/hour
-Set your own schedule
-Have fun and get paid
-Sign up at cwadultmodels.example

The theme should be similar to the website (hot pink and white). We are putting these flyers around college campuses and nightclubs.
Updates

Just uploaded a couple pics of me and my new model that might work well on the flyer(:

Target Market(s)

Our audience is attractive, young women (college students, baristas, waitresses etc.)

Industry/Entity Type

College

Requirements
Must have
• A picture of Clara Whitfield. Perhaps a long body shot on the side or just her face somewhere. Pictures can be found here: https://chirpnet.example/WhitfieldClara
and here: http://picvue.example/whitfieldclara

A visible and bold area featuring: "$100/hour"

```html
<!DOCTYPE html>
<html lang="en">
<head>
<meta charset="utf-8">
<title>Clara Whitfield Adult Models – Recruitment Flyer</title>
<link href="https://fonts.googleapis.com/css2?family=Playfair+Display:wght@900&family=Pacifico&family=Handlee&display=swap" rel="stylesheet">
<style>
  :root {
    --bg-magenta: #c23a88;
    --bg-magenta-light: #cf4f98;
    --hot-pink: #ee2a92;
    --plum-shadow: #8e2a72;
    --ink: #2a1a24;
    --white: #ffffff;
  }
  * { margin: 0; padding: 0; box-sizing: border-box; }
  html, body { width: 776px; height: 1200px; overflow: hidden; }
  body { background: var(--bg-magenta); }

  .flyer {
    position: relative;
    width: 776px;
    height: 1200px;
    overflow: hidden;
    background: radial-gradient(circle at 50% 40%, var(--bg-magenta-light), var(--bg-magenta) 75%);
  }
  .flyer__pattern {
    position: absolute; inset: 0;
    background: linear-gradient(160deg, rgba(255,255,255,0.05), rgba(255,255,255,0) 60%);
  }

  /* Brand block — fills the top area above the headline */
  .brand {
    position: absolute;
    left: 0; right: 0; top: 60px; height: 236px;
    display: flex; justify-content: center; align-items: center;
  }
  .brand__name {
    font-family: "Pacifico", cursive;
    font-size: 76px;
    color: var(--white);
    line-height: 1.3;
  }

  /* Headlines */
  .headline-pay {
    position: absolute; left: 0; right: 0; top: 318px;
    text-align: center;
    font-family: "Playfair Display", serif;
    font-weight: 900;
    font-size: 60px;
    color: var(--white);
    -webkit-text-stroke: 2px var(--hot-pink);
    text-shadow: 0 0 3px var(--white), 0 0 10px rgba(255,255,255,0.6);
  }
  .feature {
    position: absolute; left: 0; right: 0;
    text-align: center;
    font-family: "Pacifico", cursive;
    font-size: 38px;
    color: var(--white);
    -webkit-text-stroke: 1px var(--hot-pink);
    text-shadow: 0 0 4px var(--white), 0 0 10px rgba(255,255,255,0.5);
    line-height: 1.2;
  }
  .feature--schedule { top: 432px; }
  .feature--fun { top: 714px; }
  .feature--signup { top: 1064px; font-size: 36px; }

  /* Quote cards */
  .quote-card {
    position: absolute;
    display: flex;
    box-shadow: 12px 10px 0 var(--plum-shadow);
  }
  .quote-card__photo { flex: none; }
  .quote-card__mark {
    font-family: "Playfair Display", serif;
    font-weight: 900;
    line-height: 0.5;
    vertical-align: -0.25em;
  }
  .quote-card__author {
    font-family: "Handlee", cursive;
    text-align: right;
  }

  .quote-card--small {
    left: 183px; top: 504px; width: 410px; height: 179px;
    background: var(--white);
  }
  .quote-card--small .quote-card__text-wrap {
    width: 204px; padding-top: 28px;
  }
  .quote-card--small .quote-card__text {
    background: var(--hot-pink);
    color: var(--white);
    font-family: "Handlee", cursive;
    font-size: 15px;
    line-height: 1.2;
    padding: 6px 10px;
  }
  .quote-card--small .quote-card__mark { font-size: 30px; }
  .quote-card--small .quote-card__author {
    color: var(--hot-pink); font-size: 16px;
    padding: 14px 14px 0 0;
  }
  .quote-card--small .quote-card__photo {
    width: 206px; height: 179px;
    background: linear-gradient(135deg, #d9b48e, #c7876f 45%, #8a4a55);
  }

  .quote-card--large {
    left: 96px; top: 789px; width: 584px; height: 258px;
    background: var(--hot-pink);
  }
  .quote-card--large .quote-card__text-wrap {
    position: relative; width: 294px;
  }
  .quote-card--large .quote-card__text {
    position: absolute; left: 10px; top: 32px; width: 274px; height: 164px;
    background: var(--white);
    color: var(--hot-pink);
    font-family: "Handlee", cursive;
    font-size: 26px;
    line-height: 1.45;
    padding: 14px 8px 0 12px;
    white-space: nowrap;
  }
  .quote-card--large .quote-card__mark { font-size: 44px; color: var(--ink); }
  .quote-card--large .quote-card__author {
    position: absolute; right: 16px; top: 214px;
    color: var(--white); font-size: 22px;
  }
  .quote-card--large .quote-card__photo {
    width: 290px; height: 258px;
    background: linear-gradient(180deg, #8fc4ec 0%, #b9d3e3 32%, #6e7f63 42%, #2aa6d8 55%, #1a86c4 100%);
  }
</style>
</head>
<body>
<main class="flyer">
  <div class="flyer__pattern" role="img" aria-label="Repeating soft pink floral pattern background"></div>

  <header class="brand">
    <span class="brand__name">Clara Whitfield</span>
  </header>

  <h1 class="headline-pay">Pays $100/hour</h1>

  <p class="feature feature--schedule">Set your own schedule</p>

  <section class="quote-card quote-card--small">
    <div class="quote-card__text-wrap">
      <p class="quote-card__text"><span class="quote-card__mark">&ldquo;</span>Young women today are afraid of their sexuality... they're scared to express themselves. I'm here to change that <span class="quote-card__mark">&rdquo;</span></p>
      <p class="quote-card__author">-Clara Whitfield</p>
    </div>
    <div class="quote-card__photo" role="img" aria-label="Photo of two models in pink bikinis at a party"></div>
  </section>

  <p class="feature feature--fun">Have fun and get paid</p>

  <section class="quote-card quote-card--large">
    <div class="quote-card__text-wrap">
      <p class="quote-card__text"><span class="quote-card__mark">&ldquo;</span> Life doesn't have<br>to be hard. It can<br>be fun... and easy!<span class="quote-card__mark">&rdquo;</span></p>
      <p class="quote-card__author">-Clara Whitfield</p>
    </div>
    <div class="quote-card__photo" role="img" aria-label="Photo of a model in a bikini standing in a swimming pool"></div>
  </section>

  <p class="feature feature--signup">Sign up at cwadultmodels.example</p>
</main>
</body>
</html>
```